Kelvar Engineering Business Card Design

We need a new business card for our engineering consultancy, Kelvar Engineering. The card should look sharp and professional.

Kelvar Engineering is mechanical engineering consultancy providing engineering services and testing. We mainly serve the automotive enthusiast (certifying modified vehicles) and trade sectors (product development & certification). The company also provides general mechanical engineering consultancy, and services to the railway industry.

The logo attached should be used.

Location: Adelaide, South Australia

Target Market(s)

Individual Clients, and corporate clients

Industry/Entity Type

Mechanical Engineering

Requirements
Must have
• Front:

Kelvar Engineering Pty Ltd
PO Box 417
Fernhollow, SA 5093

Gavin Trelowarth MBA,BEng(Mech), MIEAust CPEng
gtrelowarth@kelvarengineering.com.au
kelvarengineering.com.au
mobile +61 (0)491 308 574

Back
Modified Vehicle Engineering & Testing
Component Design & Analysis
Individually Constructed Vehicle Engineering
Australian Design Rule (ADR) Compliance Testing
General Mechanical Engineering
Permanent Way Engineering Services
Rail Plant and Equipment Services

Nice to have
• embossing
Should not have
• Photographs or images other than the logo.

```html
<!DOCTYPE html>
<html lang="en">
<head>
<meta charset="utf-8">
<title>Kelvar Engineering – Business Card</title>
<link href="https://fonts.googleapis.com/css2?family=Saira:wght@400;500;600&display=swap" rel="stylesheet">
<style>
  :root{
    --page:#e9eaec;
    --card:#ffffff;
    --card-back:#f4f4f4;
    --navy:#1b2a4a;
    --blue:#3d86d6;
    --ink:#1d2433;
    --muted:#4a5262;
  }
  *{box-sizing:border-box;margin:0;padding:0}
  html,body{width:1200px;height:873px;overflow:hidden}
  body{background:var(--page);font-family:"Saira",sans-serif;color:var(--ink);position:relative}
  .card{position:absolute;top:271px;width:540px;height:330px;background:var(--card);
        box-shadow:0 6px 18px rgba(0,0,0,.15);overflow:hidden}
  .card--front{left:40px}
  .card--back{left:620px;background:var(--card-back)}
  .card__art{position:absolute;inset:0}

  .brand{position:absolute;display:flex;align-items:center;gap:12px}
  .brand__dot{width:46px;height:46px;border-radius:50%;background:var(--blue)}
  .brand__name{font-weight:600;font-size:22px;letter-spacing:.04em;text-transform:uppercase;color:var(--navy);white-space:nowrap}

  .card--front .brand{left:34px;top:40px}

  .details{position:absolute;right:30px;top:120px;text-align:right;color:var(--ink)}
  .details__company{font-weight:600;font-size:14px;letter-spacing:.05em;text-transform:uppercase}
  .details__address{font-size:13px;line-height:1.35}
  .person{margin-top:14px}
  .person__name{font-weight:600;font-size:21px;letter-spacing:.03em;font-variant:small-caps}
  .person__title{font-size:11px}
  .contact{list-style:none;margin-top:8px;font-size:11.5px;line-height:1.7}
  .contact li{display:flex;justify-content:flex-end;align-items:center;gap:6px;white-space:nowrap}
  .contact svg{width:13px;height:13px}

  .card--back .brand{left:170px;top:48px}
  .services{position:absolute;top:130px;left:30px;right:16px;list-style:none;
            display:grid;grid-template-columns:252px 1fr;column-gap:0;row-gap:2px;
            font-size:11.5px;line-height:1.55;color:var(--muted);align-items:baseline}
  .services li{white-space:nowrap}
  .services__lead{font-size:13.5px;color:var(--ink);font-weight:500}
  .services__small{font-size:10.5px}
  .services__wide{grid-column:1 / -1}
</style>
</head>
<body>

<section class="card card--front" aria-label="Business card front">
  <svg class="card__art" viewBox="0 0 540 330" aria-hidden="true">
    <defs>
      <linearGradient id="frontBand" x1="0" y1="0" x2="1" y2="1">
        <stop offset="0" stop-color="#a9d0f5"/>
        <stop offset="1" stop-color="#4f94df"/>
      </linearGradient>
    </defs>
    <path d="M0,250 C150,190 320,110 540,92 L540,330 L0,330 Z" fill="url(#frontBand)"/>
    <path d="M0,250 C150,190 320,110 540,92" fill="none" stroke="var(--navy)" stroke-width="6"/>
  </svg>

  <div class="brand">
    <span class="brand__dot"></span>
    <span class="brand__name">Kelvar Engineering</span>
  </div>

  <div class="details">
    <p class="details__company">Kelvar Engineering Pty Ltd</p>
    <p class="details__address">PO Box 417<br>Fernhollow, SA 5093</p>
    <div class="person">
      <p class="person__name">Gavin Trelowarth</p>
      <p class="person__title">MBA,BEng(Mech), MIEAust CPEng</p>
    </div>
    <ul class="contact">
      <li>gtrelowarth@kelvarengineering.com.au
        <svg viewBox="0 0 14 14"><circle cx="7" cy="7" r="6" fill="none" stroke="currentColor"/><rect x="3.5" y="4.5" width="7" height="5" fill="none" stroke="currentColor" stroke-width=".9"/><path d="M3.5 4.5 7 7.5 10.5 4.5" fill="none" stroke="currentColor" stroke-width=".9"/></svg></li>
      <li>kelvarengineering.com.au
        <svg viewBox="0 0 14 14"><circle cx="7" cy="7" r="6" fill="none" stroke="currentColor"/><circle cx="7" cy="7" r="3.5" fill="none" stroke="currentColor" stroke-width=".9"/><path d="M3.5 7h7M7 3.5v7" stroke="currentColor" stroke-width=".9"/></svg></li>
      <li>+61 (0)491 308 574
        <svg viewBox="0 0 14 14"><circle cx="7" cy="7" r="6" fill="none" stroke="currentColor"/><path d="M4.5 4c0 3 2.5 5.5 5.5 5.5l.5-1.3-1.6-.8-.8.8c-1-.5-1.7-1.2-2.2-2.2l.8-.8-.8-1.6z" fill="currentColor"/></svg></li>
    </ul>
  </div>
</section>

<section class="card card--back" aria-label="Business card back">
  <div class="brand">
    <span class="brand__dot"></span>
    <span class="brand__name">Kelvar Engineering</span>
  </div>

  <ul class="services">
    <li class="services__lead">Component Design &amp; Analysis</li>
    <li class="services__lead">General Mechanical Engineering</li>
    <li>Permanent Way Engineering Services</li>
    <li>Rail Plant and Equipment Services</li>
    <li>Modified Vehicle Engineering &amp; Testing</li>
    <li class="services__small">Individually Constructed Vehicle Engineering</li>
    <li class="services__wide">Australian Design Rule (ADR) Compliance Testing</li>
  </ul>
</section>

</body>
</html>
```